Solar appointment reminder card

We are looking for a new design for our appointment reminder card since we have changed our logo. The card should have the new logo along with space for the employee to hand write the customers appointment date, time, the employees name and phone number.
I've uploaded what our old basic appointment card looked like and our new logo.

The cards should be in a standard business card size and could be horizontal or vertical.

```html
<!DOCTYPE html>
<html lang="en">
<head>
<meta charset="utf-8">
<title>Bright Ridge Solar – Appointment Card</title>
<link rel="stylesheet" href="https://fonts.googleapis.com/css2?family=Montserrat:ital,wght@0,300;0,500;0,700;1,400&display=swap">
<style>
  :root {
    --page: #ffffff;
    --dark: #2c2c2e;
    --dark-deep: #1c1c1d;
    --dark-soft: #3d3d40;
    --orange: #f0761c;
    --ink: #111111;
    --white: #ffffff;
    --photo-a: #cfd3d8;
    --photo-b: #6e747c;
  }
  * { box-sizing: border-box; margin: 0; padding: 0; }
  html, body { width: 1200px; height: 1200px; overflow: hidden; background: var(--page); }
  body { position: relative; font-family: "Montserrat", sans-serif; }

  .card {
    position: absolute;
    top: 298px;
    width: 380px;
    height: 604px;
    overflow: hidden;
    box-shadow: 0 3px 8px rgba(0,0,0,0.28);
  }
  .card--front { left: 180px; background: var(--white); }
  .card--back {
    left: 640px;
    background: linear-gradient(160deg, var(--dark-deep) 0%, var(--dark) 55%, var(--dark-soft) 100%);
  }

  .card__shapes { position: absolute; inset: 0; }

  .card__title {
    position: absolute; top: 22px; width: 100%;
    text-align: center; color: #e2e2e2;
    font-weight: 300; font-size: 21px; letter-spacing: 0.3px;
  }

  .brand {
    position: absolute; left: 0; width: 100%;
    display: flex; align-items: center; justify-content: center; gap: 10px;
    color: var(--orange); font-weight: 700; font-size: 27px; letter-spacing: 0.5px;
  }
  .brand__dot { width: 18px; height: 18px; border-radius: 50%; background: var(--orange); }
  .card--front .brand { top: 112px; }
  .card--back .brand { top: 284px; }

  .photo {
    position: absolute; left: 119px; top: 201px;
    width: 142px; height: 142px; border-radius: 50%;
    border: 4px solid var(--white);
    background: radial-gradient(circle at 50% 40%, var(--photo-a), var(--photo-b));
  }

  .employee { position: absolute; top: 354px; width: 100%; text-align: center; }
  .employee__name { color: var(--orange); font-weight: 700; font-size: 25px; letter-spacing: 0.2px; }
  .employee__role { color: var(--ink); font-weight: 500; font-size: 17px; margin-top: 1px; }
  .employee__rule { width: 72px; height: 2px; background: var(--orange); margin: 7px auto 0; opacity: 0.7; }

  .details { position: absolute; top: 424px; left: 50px; border-collapse: collapse; }
  .details td { font-size: 17px; height: 28.5px; padding: 0; }
  .details__label { color: var(--orange); width: 151px; font-weight: 400; }
  .details__value { color: var(--ink); font-weight: 700; }

  .card__web {
    position: absolute; right: 24px; top: 568px;
    color: #f0f0f0; font-style: italic; font-size: 12px;
    white-space: nowrap;
  }
</style>
</head>
<body>

  <section class="card card--front" aria-label="Appointment card, front">
    <svg class="card__shapes" width="380" height="604" viewBox="0 0 380 604">
      <defs>
        <linearGradient id="headerFill" x1="0" y1="0" x2="1" y2="1">
          <stop offset="0" stop-color="#3b3b3e"/>
          <stop offset="1" stop-color="#232325"/>
        </linearGradient>
      </defs>
      <path class="header-band" d="M0 0 H380 V225 Q190 135 0 225 Z" fill="url(#headerFill)"/>
      <path class="footer-wedge" d="M40 604 Q160 530 380 534 V604 Z" fill="#232325"/>
    </svg>

    <p class="card__title">Appointment Card</p>
    <div class="brand"><span class="brand__dot"></span>Bright Ridge Solar</div>

    <div class="photo" role="img" aria-label="Employee portrait photo"></div>

    <div class="employee">
      <p class="employee__name">EMPLOYEE NAME</p>
      <p class="employee__role">Designation</p>
      <div class="employee__rule"></div>
    </div>

    <table class="details">
      <tr><td class="details__label">Date</td><td class="details__value">10 Nov 2019</td></tr>
      <tr><td class="details__label">Time</td><td class="details__value">11:40 AM</td></tr>
      <tr><td class="details__label">Representative</td><td class="details__value">Representative</td></tr>
      <tr><td class="details__label">Phone</td><td class="details__value">1234567890</td></tr>
    </table>

    <p class="card__web">www.brightridgesolar.com</p>
  </section>

  <section class="card card--back" aria-label="Appointment card, back">
    <div class="brand"><span class="brand__dot"></span>Bright Ridge Solar</div>
  </section>

</body>
</html>
```